Hotdogs & Burgers restaurant needs a new menu design

We need a new menu design for our restaurant "Pupvella". Pupvella is a fast food specialized in hotdogs and burgers.We are looking for a simple easy menu design that walk through our customer to order the sandwich ==> the fries =>> the sides and the drinks. Pupvella Menu:* Sandwiches**Hotdogs Our special fresh grilled hotdog served on fresh buns (Regular – 1.300 OMR / Franks – 2.000 OMR)*** DoganzaLettuce, tomato, jalapeno, pickle, onion, corn, chips, cheese, ketchup, mayo, mustard*** PepperBell pepper, onion, sweet chili sauce, avocado*** Chili FlamesChili carne, cheddar cheese, honey mustard*** ChicagoTomato, pickle, red onion, sweet relish, mustard*** New YorkGrilled onion, beef bacon, barbecue sauce, chili mustard*** Egg & CheeseOmelet, cheese, ketchup, mayo, mustard** Burgers 100% all natural beef & freshly ground, 100 grams each patty served on fresh buns.(Single patty - 2.000 OMR / double patty - 2.500 OMR)*** Sweet Beef BurgerBeef bacon, cheese, lettuce, tomato, pickle.*** Cheese Beef BurgerCheese, pickle, Pupvella sauce.*** Mexican Beef BurgerGuacamole sauce, red onion, lettuce, tomato, Pupvella sauce.*** Chicken BurgerFried chicken patty, lettuce, tomato, ranch sauce, Pupvella sauce== ToppingsExtra veggies 0.100 OMRExtra cheese 0.200 OMRExtra beef Bacon 0.400 OMRExtra patty 0.500 OMR*Fries**Regular 0.600 OMR**Crispy 0.800 OMR**Wedges 0.800 OMR**Chili fries 1.500 OMRTopped with our chili carne, cheddar cheese, jalapeno, honey mustard**Lava fries 1.500 OMRTopped with fried bacon, fried onion, cheddar cheese, ranch sauce*Sides**Crispy strips 1.800 OMR5 pieces of chicken strips topped with BBQ sauce or honey mustard sauce, Pupvella side sauce**Jalapeno cheese balls 1.300 OMR6 pieces of jalapeno cheese balls, sweet chili side sauce**Nachos 1.500 OMRA plate of nachos topped with cheddar cheese and jalapeno*Drinks**Flavored sparkling cans 0.800 OMR **Fresh orange juice 1.400 OMR**Mineral water 0.300 OMR**Soft drink 0.400 OMR**Mojito 1.500 OMRThe menu should not have any of our products pictures (icons/symbols proffered). we would prefer if the designs have unique icons/symbols created for Pupvella. you can check our Picturo page https://www.picturo-app.example/pupvella.official/

Industry/Entity Type

American Restaurant

Colors

Designer to choose colors to be used in the design.

Requirements
Must have
• Pupvella Logo, Icons

```html
<!DOCTYPE html>
<html lang="en">
<head>
<meta charset="utf-8">
<title>Pupvella Menu</title>
<link href="https://fonts.googleapis.com/css2?family=Bungee&family=Montserrat:wght@400;500;600;700&family=Oswald:wght@600&display=swap" rel="stylesheet">
<style>
  :root {
    --paper: #ffffff;
    --board: #2a1f27;
    --board-light: #3b2c36;
    --yellow: #f3ec0d;
    --ink: #ffffff;
    --ink-dark: #1c1519;
    --muted: #e9e4e7;
  }
  * { margin: 0; padding: 0; box-sizing: border-box; }
  html, body { width: 959px; height: 1200px; overflow: hidden; background: var(--paper); }
  body { position: relative; font-family: "Montserrat", sans-serif; color: var(--ink); }
  .board {
    position: absolute; left: 73px; top: 76px; width: 818px; height: 1058px;
    background: radial-gradient(ellipse at 45% 40%, var(--board-light) 0%, var(--board) 70%);
    overflow: hidden;
  }
  .abs { position: absolute; }
  .brand {
    position: absolute; left: 0; width: 959px; top: 170px; text-align: center;
    font-family: "Bungee", sans-serif; font-size: 54px; color: var(--yellow); letter-spacing: 1px;
  }
  .badge {
    position: absolute; width: 78px; height: 78px; border-radius: 50%;
    background: var(--paper); border: 3px solid var(--ink-dark); box-shadow: 0 0 0 2px var(--paper);
  }
  .banner { position: absolute; }
  .banner-title {
    position: absolute; font-family: "Bungee", sans-serif; font-size: 26px;
    color: var(--ink-dark); line-height: 1;
  }
  .txt { position: absolute; font-size: 12px; line-height: 14px; }
  .name { font-weight: 600; text-transform: uppercase; }
  .desc { font-weight: 400; color: var(--muted); }
  .lead { color: var(--yellow); font-weight: 600; }
  .price { position: absolute; color: var(--yellow); font-weight: 600; font-size: 12px; line-height: 14px; }
  .bold { font-weight: 600; }
  .frame { position: absolute; border: 2px solid var(--paper); }
  .dots-v {
    position: absolute; left: 469px; top: 292px; width: 7px; height: 604px;
    background: radial-gradient(circle, var(--paper) 2.6px, transparent 3px) 0 0 / 7px 10.5px repeat-y;
  }
  .dots-h {
    position: absolute; left: 512px; top: 1051px; width: 338px; height: 6px;
    background: radial-gradient(circle, var(--paper) 2.2px, transparent 2.6px) 0 0 / 8px 6px repeat-x;
  }
  .rule { position: absolute; left: 522px; top: 606px; width: 320px; height: 2px; background: var(--paper); }
  .toppings-title {
    position: absolute; left: 528px; top: 622px; font-family: "Oswald", sans-serif;
    font-size: 26px; color: var(--yellow); letter-spacing: 1px;
  }
  .topping-icon {
    position: absolute; top: 626px; width: 26px; height: 26px; border-radius: 50%;
    border: 2px solid var(--yellow);
  }
  .social-dot { position: absolute; top: 1080px; width: 22px; height: 22px; border-radius: 50%; background: var(--yellow); }
  .social { position: absolute; top: 1084px; font-size: 12px; color: var(--muted); }
</style>
</head>
<body>
  <div class="board"></div>

  <div class="brand">PUPVELLA</div>

  <!-- Banners -->
  <svg class="banner" style="left:180px;top:284px" width="254" height="42" viewBox="0 0 254 42"><polygon points="0,2 240,0 232,10 254,20 238,28 246,42 0,40" fill="var(--yellow)"/></svg>
  <svg class="banner" style="left:180px;top:696px" width="254" height="40" viewBox="0 0 254 40"><polygon points="0,2 236,0 228,10 254,22 236,28 248,40 0,38" fill="var(--yellow)"/></svg>
  <svg class="banner" style="left:180px;top:942px" width="254" height="40" viewBox="0 0 254 40"><polygon points="0,2 240,0 230,12 254,20 240,30 252,40 0,38" fill="var(--yellow)"/></svg>
  <svg class="banner" style="left:592px;top:284px" width="258" height="42" viewBox="0 0 258 42"><polygon points="0,2 258,0 240,14 254,26 236,42 0,40" fill="var(--yellow)"/></svg>
  <svg class="banner" style="left:588px;top:784px" width="262" height="42" viewBox="0 0 262 42"><polygon points="0,2 262,0 246,14 258,24 240,30 262,42 0,40" fill="var(--yellow)"/></svg>

  <div class="badge" style="left:103px;top:261px" role="img" aria-label="Hotdog icon"></div>
  <div class="badge" style="left:519px;top:261px" role="img" aria-label="Burger icon"></div>
  <div class="badge" style="left:103px;top:671px" role="img" aria-label="Fries icon"></div>
  <div class="badge" style="left:505px;top:761px" role="img" aria-label="Sides bowl icon"></div>
  <div class="badge" style="left:103px;top:921px" role="img" aria-label="Drink cup icon"></div>

  <div class="banner-title" style="left:194px;top:292px">SANDWICHES</div>
  <div class="banner-title" style="left:604px;top:292px">BURGERS</div>
  <div class="banner-title" style="left:194px;top:703px">FRIES</div>
  <div class="banner-title" style="left:600px;top:791px">SIDES</div>
  <div class="banner-title" style="left:194px;top:949px">DRINKS</div>

  <div class="dots-v"></div>

  <!-- Sandwiches -->
  <div class="txt lead" style="left:107px;top:348px">Hotdogs<br>Our special fresh grilled hotdog served on fresh buns<br>Regular – 1.300 OMR | Franks – 2.000 OMR)</div>
  <div class="txt" style="left:107px;top:404px"><div class="name">Pupvella</div><div class="desc">Lettuce, tomato, jalapeno, pickle, onion, corn, chips,<br>cheese, ketchup, mayo, mustard</div></div>
  <div class="txt" style="left:107px;top:461px"><div class="name">Pepper</div><div class="desc">Bell pepper, onion, sweet chili sauce, avocado</div></div>
  <div class="txt" style="left:107px;top:503px"><div class="name">Chili Flames</div><div class="desc">Chili carne, cheddar cheese, honey mustard</div></div>
  <div class="txt" style="left:107px;top:545px"><div class="name">Chicago</div><div class="desc">Tomato, pickle, red onion, sweet relish, mustard</div></div>
  <div class="txt" style="left:107px;top:588px"><div class="name">New York</div><div class="desc">Grilled onion, beef bacon, barbecue sauce, chili mustard</div></div>
  <div class="txt" style="left:107px;top:635px"><div class="name">Egg &amp; Cheese</div><div class="desc">Omelet, cheese, ketchup, mayo, mustard</div></div>

  <!-- Fries -->
  <div class="txt bold" style="left:107px;top:759px">Regular<br>Crispy<br>Wedges</div>
  <div class="price" style="left:365px;top:759px">0.600 OMR<br>0.800 OMR<br>0.800 OMR</div>
  <div class="txt" style="left:107px;top:816px"><div class="name">Chili Fries 1.500 OMR</div><div class="desc">Topped with our chili carne, cheddar<br>cheese, jalapeno, honey mustard</div></div>
  <div class="price" style="left:365px;top:816px">1.500 OMR</div>
  <div class="txt" style="left:107px;top:872px"><div class="name">Lava Fries 1.500 OMR</div><div class="desc">Topped with fried bacon, fried onion,<br>cheddar cheese, ranch sauce</div></div>
  <div class="price" style="left:365px;top:872px">1.500 OMR</div>

  <!-- Drinks -->
  <div class="frame" style="left:102px;top:956px;width:370px;height:136px;border-top:none"></div>
  <div class="txt name" style="left:121px;top:1010px">Flavored sparkling cans<br>Fresh orange juice<br>Mineral water<br>Soft drink<br>Mojito</div>
  <div class="price" style="left:365px;top:1010px">0.800 OMR<br>1.400 OMR<br>0.300 OMR<br>0.400 OMR<br>1.500 OMR</div>

  <!-- Burgers -->
  <div class="frame" style="left:506px;top:308px;width:358px;height:442px;border-top:none"></div>
  <div class="txt lead" style="left:522px;top:348px">100% all natural beef &amp; freshly ground, 100 grams each<br>patty served on fresh buns.<br>(Single patty - 2.000 OMR | Double patty - 2.500 OMR)</div>
  <div class="txt" style="left:522px;top:410px"><div class="name">Sweet Beef Burger</div><div class="desc">Beef bacon, cheese, lettuce, tomato, pickle.</div></div>
  <div class="txt" style="left:522px;top:452px"><div class="name">Cheese Beef Burger</div><div class="desc">Cheese, pickle, Pupvella sauce.</div></div>
  <div class="txt" style="left:522px;top:494px"><div class="name">Mexican Beef Burger</div><div class="desc">Guacamole sauce, red onion, lettuce, tomato, Pupvella<br>sauce.</div></div>
  <div class="txt" style="left:522px;top:550px"><div class="name">&nbsp;Chicken Burger</div><div class="desc">Fried chicken patty, lettuce, tomato, ranch sauce,<br>Pupvella sauce</div></div>
  <div class="rule"></div>
  <div class="toppings-title">TOPPINGS</div>
  <div class="topping-icon" style="left:716px" role="img" aria-label="Veggies icon"></div>
  <div class="topping-icon" style="left:754px" role="img" aria-label="Cheese icon"></div>
  <div class="topping-icon" style="left:786px" role="img" aria-label="Bacon icon"></div>
  <div class="topping-icon" style="left:820px" role="img" aria-label="Patty icon"></div>
  <div class="txt bold" style="left:522px;top:664px">Extra veggies<br>Extra cheese<br>Extra beef Bacon<br>Extra patty</div>
  <div class="price" style="left:778px;top:664px">0.100 OMR<br>0.200 OMR<br>0.400 OMR<br>0.500 OMR</div>

  <!-- Sides -->
  <div class="txt" style="left:505px;top:852px"><div class="lead">Crispy strips</div><div class="desc">5 pieces of chicken strips topped with<br>BBQ sauce or honey mustard sauce,<br>Pupvella side sauce</div></div>
  <div class="price" style="left:770px;top:852px">1.800 OMR</div>
  <div class="txt" style="left:505px;top:923px"><div class="lead name">Jalapeno cheese balls</div><div class="desc">6 pieces of jalapeno cheese balls, sweet<br>chili side sauce</div></div>
  <div class="price" style="left:770px;top:923px">1.300 OMR</div>
  <div class="txt" style="left:505px;top:979px"><div class="lead name">Nachos</div><div class="desc">A plate of nachos topped with cheddar<br>cheese and jalapeno</div></div>
  <div class="price" style="left:770px;top:979px">1.500 OMR</div>

  <div class="dots-h"></div>

  <div class="social-dot" style="left:503px"></div>
  <a class="social" style="left:540px;text-decoration:none" href="https://www.picturo-app.example/pupvella.official/">@pupvella.official</a>
  <div class="social-dot" style="left:742px"></div>
  <div class="social" style="left:780px">/pupvella</div>
</body>
</html>
```